Meridian Rest Supply Needs Business Card

Looking for a very nice looking business card. Creative but not extravagant. We sell beds and pillows across the U.S. and need something professional but catchy. I have attached the logo.

Name : Dale Fenwick
Title : President
Phone : (800) 417-2964
Email: sleep@quorvana.com
Website: www.quorvana.com

Can be single-sided or double-sided
horizontal or vertical

Can use Blues/Greys

Target Market(s)

Mass Market

Industry/Entity Type

Retail

Contact Information for Business Card

Name : Dale Fenwick
Title : President
Phone : (800) 417-2964
Email: sleep@quorvana.com
Website: www.quorvana.com

Requirements
Must have
• Clean, Modern, Smooth
• Can use Blues/Greys
• On the other side without the information - have something simple like www.quorvana.com or our logo
Nice to have
• Surprise me
Should not have
• Nothing crazy, nothing cluttered

```html
<!DOCTYPE html>
<html lang="en">
<head>
<meta charset="utf-8">
<title>Quorvana Business Card</title>
<link href="https://fonts.googleapis.com/css2?family=Montserrat:wght@300;400;500&display=swap" rel="stylesheet">
<style>
  :root {
    --canvas-bg: #efefef;
    --card-dark-top: #1c2830;
    --card-dark-bottom: #2d3c47;
    --brand-blue: #2f98d0;
    --brand-blue-light: #39a4dc;
    --divider-white: #e8ecef;
    --text-white: #f2f4f6;
    --text-muted: #d9dee2;
  }
  * { box-sizing: border-box; margin: 0; padding: 0; }
  html, body { width: 1200px; height: 800px; overflow: hidden; }
  body {
    background: var(--canvas-bg);
    font-family: "Montserrat", sans-serif;
    display: flex;
    align-items: center;
    justify-content: center;
    gap: 40px;
  }
  .card {
    position: relative;
    width: 540px;
    height: 310px;
    border-radius: 20px;
    overflow: hidden;
    background: linear-gradient(180deg, var(--card-dark-top), var(--card-dark-bottom));
    box-shadow: 0 6px 18px rgba(0,0,0,0.18);
  }
  .card-wave { position: absolute; inset: 0; width: 100%; height: 100%; }
  .wordmark {
    position: absolute;
    font-weight: 300;
    letter-spacing: 2px;
  }
  .card-front .wordmark {
    top: 44px; left: 46px;
    font-size: 40px;
    color: var(--text-white);
  }
  .contact {
    position: absolute;
    top: 112px; left: 300px;
    color: var(--text-white);
  }
  .contact-name { font-size: 21px; font-weight: 400; letter-spacing: 0.5px; }
  .contact-title { font-size: 15px; color: var(--brand-blue); margin-bottom: 10px; }
  .contact-line {
    display: flex; align-items: center; gap: 8px;
    font-size: 14px; color: var(--text-muted); line-height: 24px;
  }
  .contact-line svg { width: 13px; height: 13px; flex: none; }
  .card-back .wordmark {
    top: 92px; left: 0; right: 0;
    text-align: center;
    font-size: 66px;
    color: var(--brand-blue-light);
    letter-spacing: 6px;
  }
  .back-url {
    position: absolute;
    top: 192px; left: 110px;
    font-size: 13px;
    letter-spacing: 1px;
    color: var(--text-muted);
  }
</style>
</head>
<body>
  <section class="card card-front">
    <svg class="card-wave" viewBox="0 0 540 310" preserveAspectRatio="none" aria-hidden="true">
      <path d="M0,168 C120,156 200,230 290,272 C350,300 400,308 440,310 L0,310 Z" fill="var(--divider-white)"/>
      <path d="M0,176 C118,164 196,238 286,280 C344,304 392,310 430,310 L0,310 Z" fill="var(--brand-blue)"/>
    </svg>
    <div class="wordmark">quorvana</div>
    <div class="contact">
      <div class="contact-name">Dale Fenwick</div>
      <div class="contact-title">President</div>
      <div class="contact-line">
        <svg viewBox="0 0 16 16"><rect x="1" y="4" width="14" height="10" rx="2" fill="var(--brand-blue)"/><rect x="4" y="1" width="8" height="4" rx="1.5" fill="var(--brand-blue)"/><circle cx="8" cy="9" r="2.4" fill="var(--card-dark-top)"/></svg>
        (800) 417-2964
      </div>
      <div class="contact-line">
        <svg viewBox="0 0 16 16"><rect x="1" y="3" width="14" height="10" rx="1" fill="var(--brand-blue)"/><path d="M1.5,3.5 L8,9 L14.5,3.5" stroke="var(--card-dark-top)" stroke-width="1.3" fill="none"/></svg>
        sleep@quorvana.com
      </div>
      <div class="contact-line">
        <svg viewBox="0 0 16 16"><circle cx="8" cy="8" r="6.5" fill="none" stroke="var(--brand-blue)" stroke-width="1.4"/><ellipse cx="8" cy="8" rx="2.8" ry="6.5" fill="none" stroke="var(--brand-blue)" stroke-width="1.1"/><line x1="1.5" y1="8" x2="14.5" y2="8" stroke="var(--brand-blue)" stroke-width="1.1"/></svg>
        www.quorvana.com
      </div>
    </div>
  </section>

  <section class="card card-back">
    <div class="wordmark">quorvana</div>
    <div class="back-url">www.quorvana.com</div>
  </section>
</body>
</html>
```